Messestand für Start-Up
Zielgruppe
Norbelkau
Ergänzungsfuttermittel
Snack's, Kauartikel und mehr
Wir sind ein junges Start-Up Unternehmen und produzieren hochwertige Ergänzungsfuttermittel für Hunde und Katzen.
Unsere Zielgruppe sind hauptsächlich Hundebesitzer. Wir möchten zu unserem hochwertigen Logo ein exklusives und edles Auftreten bei einer Messe mit zwei Roll-Ups und einer Messetheke.
Maße der Theke: https://www.plattenwerk-kolm.de/hochwertige-messetheke-gebogen-inkl-druck-und-versand.html?auflage=27431158&
Maße der Roll-Ups (Info: Wir möchten zwei Roll-Ups jeweils 100x200cm): https://www.brennhaus-medien.de/displaysysteme/rollup-displays/rollup-duo-outdoor.aspx
Es dürfen alle Produktbilder unter der Kategorie 'Snack's und Kauartikel' von unserer Website verwendet werden.
https://www.norbelkau.de/booster/Snacks-&-Kauartikel-c248716093
Aufgabenstellung
Zwei Roll Ups je 100x200cm + Messetheke
Wir möchten ein hochwertiges auftreten

```html
<!DOCTYPE html>
<html lang="de">
<head>
<meta charset="utf-8">
<title>Norbelkau – Messeauftritt</title>
<link href="https://fonts.googleapis.com/css2?family=Barlow+Condensed:wght@500;600&display=swap" rel="stylesheet">
<style>
  :root {
    --stage: #373737;
    --print-black: #000000;
    --ink-white: #ffffff;
    --brand-beige: #d8bc9c;
    --counter-dark: #232323;
    --counter-mid: #3e3e3e;
    --dog-brown: #8a4a1e;
    --dog-white: #cfc8c0;
    --cat-amber: #a8782f;
    --cat-dark: #3d2a12;
  }
  * { margin: 0; padding: 0; box-sizing: border-box; }
  html, body { width: 1200px; height: 1001px; overflow: hidden; }
  body {
    background: var(--stage);
    font-family: "Barlow Condensed", "Arial Narrow", sans-serif;
    color: var(--ink-white);
    position: relative;
  }

  /* Roll-up faces */
  .rollup {
    position: absolute;
    top: 257px;
    width: 181px;
    height: 426px;
    background: var(--print-black);
    overflow: hidden;
  }
  .rollup--dog { left: 221px; }
  .rollup--cat { left: 798px; }

  .rollup__tagline {
    position: absolute;
    top: 10px; left: 0; right: 0;
    text-align: center;
    font-weight: 600;
    font-size: 10.5px;
    letter-spacing: 0.1px;
  }
  .rollup__photo {
    position: absolute;
    left: 0; right: 0; top: 90px; bottom: 0;
  }
  .rollup--dog .rollup__photo {
    background:
      radial-gradient(ellipse 45% 30% at 55% 42%, var(--dog-white) 0%, transparent 70%),
      radial-gradient(ellipse 60% 45% at 55% 35%, var(--dog-brown) 0%, transparent 75%),
      linear-gradient(180deg, var(--print-black) 0%, #2a1a10 45%, #6d6a66 80%, #1a1a1a 100%);
  }
  .rollup--cat .rollup__photo {
    background:
      radial-gradient(ellipse 60% 45% at 50% 40%, var(--cat-amber) 0%, transparent 78%),
      linear-gradient(180deg, var(--print-black) 0%, var(--cat-dark) 40%, #6b4a1e 75%, #1a1208 100%);
  }

  .brand {
    position: absolute;
    left: 0; right: 0;
    text-align: center;
  }
  .brand__emblem {
    display: block;
    margin: 0 auto;
    border-radius: 50%;
    background: radial-gradient(circle at 50% 50%, #2c2c2c 0%, #141414 70%, transparent 72%),
                linear-gradient(90deg, #8c6b50, #cfcfcf 40%, #555 60%, #2a2a2a);
  }
  .brand__name {
    display: block;
    font-weight: 500;
    color: var(--brand-beige);
    line-height: 1;
  }
  .brand__url {
    display: block;
    font-weight: 500;
    color: var(--brand-beige);
  }

  .rollup .brand { top: 40px; }
  .rollup .brand__emblem { width: 107px; height: 42px; border-radius: 22px; }
  .rollup .brand__name { font-size: 27px; margin-top: 6px; }
  .rollup .brand__url { font-size: 6.5px; margin-top: 1px; }

  .rollup__hashtags {
    position: absolute;
    left: 19px;
    top: 309px;
    list-style: none;
    font-weight: 600;
    font-size: 15px;
    line-height: 17.7px;
    text-shadow: 0 0 6px rgba(0,0,0,0.4);
  }

  /* Counter front */
  .counter__top {
    position: absolute;
    left: 462px; top: 494px;
    width: 273px; height: 6px;
    background: var(--brand-beige);
  }
  .counter {
    position: absolute;
    left: 476px; top: 500px;
    width: 245px; height: 202px;
    overflow: hidden;
  }
  .counter__texture {
    position: absolute; inset: 0;
    background:
      linear-gradient(90deg, var(--counter-mid) 0%, var(--counter-dark) 18%, #1c1c1c 50%, var(--counter-dark) 82%, var(--counter-mid) 100%);
  }
  .counter .brand { top: 25px; }
  .counter .brand__emblem { width: 127px; height: 46px; border-radius: 24px; }
  .counter .brand__name { font-size: 30px; margin-top: 8px; }
  .counter__claim {
    position: absolute; left: 0; right: 0; top: 118px;
    text-align: center;
    font-weight: 500;
    font-size: 11.5px;
  }
  .counter__benefits {
    position: absolute; left: 0; right: 0; top: 134px;
    text-align: center;
    font-weight: 500;
    font-size: 8.6px;
    color: var(--brand-beige);
  }
  .counter__benefits span + span { margin-left: 3px; }
  .counter__url {
    position: absolute; left: 0; right: 0; top: 162px;
    text-align: center;
    font-weight: 500;
    font-size: 11.5px;
  }
</style>
</head>
<body>

  <section class="rollup rollup--dog">
    <div class="rollup__photo" role="img" aria-label="Portraitfoto eines fröhlichen braun-weißen Hundes vor schwarzem Hintergrund"></div>
    <p class="rollup__tagline">SNACKS, KAUARTIKEL, BOOSTER &amp; MEHR</p>
    <div class="brand">
      <span class="brand__emblem" role="img" aria-label="Polygon-Illustration eines Hunde- und Katzenkopfes"></span>
      <span class="brand__name">Norbelkau</span>
      <span class="brand__url">www.norbelkau.de</span>
    </div>
    <ul class="rollup__hashtags">
      <li>#TIERLIEBE</li>
      <li>#VITALITÄT</li>
      <li>#EINZIGARTIG</li>
      <li>#LEBENSQUALITÄT</li>
    </ul>
  </section>

  <div class="counter__top"></div>
  <section class="counter">
    <div class="counter__texture" role="img" aria-label="Dunkles Polygonmuster in Grautönen"></div>
    <div class="brand">
      <span class="brand__emblem" role="img" aria-label="Polygon-Illustration eines Hunde- und Katzenkopfes"></span>
      <span class="brand__name">Norbelkau</span>
    </div>
    <p class="counter__claim">ERGÄNZUNGSFUTTERMITTEL UND MEHR</p>
    <p class="counter__benefits">
      <span>✓ Agilität</span><span>✓ Leistung</span><span>✓ Gesundheit</span><span>✓ Mobilität</span>
    </p>
    <p class="counter__url">www.norbelkau.de</p>
  </section>

  <section class="rollup rollup--cat">
    <div class="rollup__photo" role="img" aria-label="Portraitfoto einer getigerten Bengalkatze, die sich das Maul leckt, vor schwarzem Hintergrund"></div>
    <p class="rollup__tagline">SNACKS, KAUARTIKEL, BOOSTER &amp; MEHR</p>
    <div class="brand">
      <span class="brand__emblem" role="img" aria-label="Polygon-Illustration eines Hunde- und Katzenkopfes"></span>
      <span class="brand__name">Norbelkau</span>
      <span class="brand__url">www.norbelkau.de</span>
    </div>
    <ul class="rollup__hashtags">
      <li>#NATÜRLICH</li>
      <li>#REGENERIEREND</li>
      <li>#AUFBAUEND</li>
      <li>#TIERGESUNDHEIT</li>
    </ul>
  </section>

</body>
</html>
```